letter head for a construction company

Company Name: Kaleshi Construction Limited

Address: Tumbili Street, Kigamboni Shores, Dar es salaam, Tanzania

Phone: 0754382916

email : info@kaleshiconstruction.example

website : www.kaleshiconstruction.example

```html
<!DOCTYPE html>
<html lang="en">
<head>
<meta charset="utf-8">
<title>Kaleshi Construction Limited – Letterhead</title>
<link rel="stylesheet" href="https://fonts.googleapis.com/css2?family=Source+Sans+3:wght@400;600;700&display=swap">
<style>
  :root {
    --backdrop: #f1f2f1;
    --paper: #ffffff;
    --ink: #3a3a3a;
    --brand-dark: #3d3f42;
    --orange: #f08a00;
    --orange-deep: #ec6c00;
    --orange-light: #f6a623;
    --rule: #333333;
  }
  html, body {
    margin: 0;
    padding: 0;
    width: 1052px;
    height: 1200px;
    overflow: hidden;
    background: var(--backdrop);
    font-family: "Source Sans 3", sans-serif;
  }
  .letterhead {
    position: absolute;
    left: 244px;
    top: 201px;
    width: 564px;
    height: 799px;
    background: var(--paper);
    overflow: hidden;
    color: var(--ink);
  }
  .brand-name {
    position: absolute;
    left: 32px;
    top: 30px;
    margin: 0;
    width: 150px;
    font-size: 15px;
    line-height: 16px;
    font-weight: 700;
    letter-spacing: 0.4px;
    text-transform: uppercase;
    color: var(--brand-dark);
  }
  .pattern-top {
    position: absolute;
    left: 228px;
    top: 0;
    width: 336px;
    height: 116px;
  }
  .pattern-bottom {
    position: absolute;
    left: 0;
    top: 670px;
    width: 423px;
    height: 129px;
  }
  .subject {
    position: absolute;
    left: 23px;
    top: 123px;
    margin: 0;
    font-size: 10.5px;
    line-height: 12px;
  }
  .subject strong { color: var(--orange); font-weight: 700; display: block; }
  .salutation {
    position: absolute;
    left: 23px;
    top: 179px;
    margin: 0;
    font-size: 10.5px;
    font-weight: 700;
    color: var(--orange);
  }
  .body-copy {
    position: absolute;
    left: 23px;
    top: 202px;
    width: 510px;
    font-size: 10.3px;
    line-height: 15.4px;
  }
  .body-copy p { margin: 0 0 29px; }
  .sign-off {
    position: absolute;
    left: 229px;
    top: 555px;
    width: 105px;
    text-align: center;
  }
  .sign-off .signature-mark {
    display: block;
    margin: 0 auto;
    width: 60px;
    height: 44px;
  }
  .sign-off .line { border-top: 1px solid var(--rule); margin-top: 1px; }
  .sign-off .label {
    font-size: 7.5px;
    color: var(--orange);
    letter-spacing: 0.2px;
    margin-top: 3px;
  }
  .contact {
    position: absolute;
    left: 40px;
    top: 735px;
    margin: 0;
    font-size: 10px;
    line-height: 12px;
    color: #ffffff;
    font-style: normal;
  }
</style>
</head>
<body>
  <main class="letterhead">
    <h1 class="brand-name">Kaleshi Construction Limited</h1>

    <svg class="pattern-top" viewBox="0 0 336 116" role="img" aria-label="Decorative cluster of orange triangles">
      <defs>
        <linearGradient id="topFade" x1="0" y1="0" x2="1" y2="0">
          <stop offset="0" stop-color="#f6a623" stop-opacity="0"/>
          <stop offset="0.25" stop-color="#f6a623" stop-opacity="0.85"/>
          <stop offset="1" stop-color="#ec6c00"/>
        </linearGradient>
      </defs>
      <rect width="336" height="116" fill="url(#topFade)"/>
    </svg>

    <p class="subject"><strong>Lorem Ipsum is simply</strong>dummy text of the printing</p>

    <p class="salutation">Dear Client,</p>

    <section class="body-copy">
      <p>Lorem Ipsum is simply dummy text of the printing and typesetting industry. Lorem Ipsum has been the industry's standard dummy text ever since the 1500s, when an unknown printer took a galley of type and scrambled it to make a type specimen book. It has survived not only five centuries, but also the leap into electronic typesetting, remaining essentially unchanged. It was popularised in the 1960s with the release of Letraset sheets containing Lorem Ipsum passages, and more recently with desktop publishing software like Aldus PageMaker including versions of Lorem Ipsum.</p>
      <p>Lorem Ipsum is simply dummy text of the printing and typesetting industry. Lorem Ipsum has been the industry's standard dummy text ever since the 1500s, when an unknown printer took a galley of type and scrambled</p>
      <p>Lorem Ipsum is simply dummy text of the printing and typesetting industry. Lorem Ipsum has been the industry's standard dummy text ever since the 1500s, when an unknown printer took a galley of type and scrambled it to make a type specimen book. It has survived not only five centuries, but also the leap into electronic typesetting, remaining essentially unchanged. It was popularised in the 1960s with the release of Letraset sheets containing Lorem Ipsum passages, and more recently with desktop publishing software like Aldus PageMaker including versions of Lorem Ipsum.</p>
    </section>

    <div class="sign-off">
      <svg class="signature-mark" viewBox="0 0 60 44" role="img" aria-label="Handwritten signature">
        <rect width="60" height="44" fill="#e6e6e6"/>
      </svg>
      <div class="line"></div>
      <div class="label">SIGNATURE</div>
    </div>

    <svg class="pattern-bottom" viewBox="0 0 423 129" role="img" aria-label="Decorative cluster of orange triangles">
      <defs>
        <linearGradient id="bottomFade" x1="0" y1="1" x2="1" y2="0">
          <stop offset="0" stop-color="#ec6c00"/>
          <stop offset="0.6" stop-color="#f08a00" stop-opacity="0.9"/>
          <stop offset="1" stop-color="#f6a623" stop-opacity="0"/>
        </linearGradient>
      </defs>
      <rect width="423" height="129" fill="url(#bottomFade)"/>
    </svg>

    <address class="contact">
      Tumbili Street, Kigamboni Shores, Dar es salaam, Tanzania<br>
      0754382916<br>
      info@kaleshiconstruction.example<br>
      www.kaleshiconstruction.example
    </address>
  </main>
</body>
</html>
```